Mirova Coffee Beans

I need a label design for our coffee beans brand. The labels would be stuck on a neutral black valve packaging. The labels have a size of 10 × 20 cm.
1 variety: Café Tramo 60/40
2 variety: Café Sorrel 70/30
3 variety: Café Tiva 80/20
4 variety: Café Wisp 100%
5 varieties: Espresso Vasto 50/50
6 varieties: Espresso Calmora 60/40
7 variety: Espresso Nevio 80/20
8 variety: Brisa Kalumetos (specially roasted for Freddo Espresso / Cappuccino)

For example, 70/30 means 70%Arabica 30%Robusta

every label must say: www.tessuna.de Tessuna
Lindenkamp-Weg-Str. 7
47618 Hollerbeck, whole roasted coffee beans, store in a cool dry place , But in german (www.tessuna.de Tessuna
Lindenkamp-Weg-Str. 7
47618 Hollerbeck, whole coffee beans roasted, store in a cool, dry place)

the labels should be plain and all in a different color

Target Market(s)

Coffee beans

Requirements
Must have
• our logo see attachment! the coffee varieties white label black writing! the espresso varieties black label white writing!
Nice to have
• Modern, perhaps with numbers like 70/30 on a large scale
Should not have
• characters

```html
<!DOCTYPE html>
<html lang="de">
<head>
<meta charset="utf-8">
<title>Tessuna – Etiketten</title>
<link rel="stylesheet" href="https://fonts.googleapis.com/css2?family=Cinzel:wght@500&family=Cormorant+SC:wght@500&family=Montserrat:wght@400;500;700&display=swap">
<style>
  :root {
    --backdrop: #e9ebec;
    --paper-light: #ffffff;
    --ink-light: #111111;
    --paper-dark: #000000;
    --ink-dark: #ffffff;
    --tramo: #f8d8bc;
    --sorrel: #8b5e3c;
    --tiva: #dfa066;
    --wisp: #c27a55;
    --vasto: #7f8ea8;
    --calmora: #b59a0c;
    --nevio: #0f6b14;
    --brisa: #5e0f4f;
  }
  * { margin: 0; padding: 0; box-sizing: border-box; }
  html, body { width: 1200px; height: 1200px; overflow: hidden; }
  body {
    background: var(--backdrop);
    font-family: "Montserrat", sans-serif;
    display: grid;
    grid-template-columns: repeat(4, 230px);
    grid-template-rows: repeat(2, 460px);
    column-gap: 60px;
    row-gap: 100px;
    padding: 90px 50px;
  }
  .label {
    position: relative;
    width: 230px;
    height: 460px;
    background: var(--paper-light);
    color: var(--ink-light);
    --rule: var(--ink-light);
  }
  .label--espresso {
    background: var(--paper-dark);
    color: var(--ink-dark);
    --rule: var(--ink-dark);
  }
  .brand {
    position: absolute;
    top: 28px; left: 0; right: 0;
    text-align: center;
    font-family: "Cinzel", serif;
    font-weight: 500;
    font-size: 30px;
    letter-spacing: 1px;
  }
  .brand-rule {
    position: absolute;
    top: 90px; left: 42px;
    width: 146px; height: 1px;
    background: var(--rule);
  }
  .variety {
    position: absolute;
    top: 118px; left: 0; right: 0;
    text-align: center;
    font-weight: 500;
    font-size: 17px;
    line-height: 17px;
    letter-spacing: 0.6px;
    text-transform: uppercase;
  }
  .blend {
    position: absolute;
    top: 296px; left: 0; right: 10px;
  }
  .blend-swatch {
    position: absolute;
    left: 0; top: 0;
    width: 12px; height: 30px;
    background: var(--swatch);
  }
  .blend-ratio {
    padding-left: 16px;
    font-size: 19px;
    line-height: 20px;
    letter-spacing: 1.2px;
  }
  .blend-ratio--note { font-size: 13.5px; letter-spacing: 1px; }
  .blend-detail {
    padding-left: 16px;
    font-size: 6.5px;
    letter-spacing: 0.4px;
    margin-top: 2px;
    text-transform: uppercase;
  }
  .blend-detail--note { font-size: 7.5px; }
  .beans-note {
    position: absolute;
    top: 398px; left: 18px;
    display: flex; align-items: center; gap: 4px;
    font-weight: 700;
    font-size: 6px;
    line-height: 7px;
    letter-spacing: 0.5px;
    text-transform: uppercase;
  }
  .beans-note svg { width: 16px; height: 10px; }
  .address {
    position: absolute;
    top: 419px; left: 19px;
    font-family: "Cormorant SC", serif;
    font-weight: 500;
    font-size: 7px;
    line-height: 7px;
  }
  .web {
    position: absolute;
    top: 437px; left: 19px;
    font-weight: 500;
    font-size: 8px;
  }
  .weight {
    position: absolute;
    top: 418px; right: 14px;
    font-size: 20px;
    line-height: 20px;
    text-align: right;
  }
  .weight small {
    display: block;
    font-size: 6px;
    line-height: 8px;
    font-weight: 500;
  }
</style>
</head>
<body>

<section class="label label--cafe" style="--swatch: var(--tramo)">
  <div class="brand">TESSUNA</div>
  <div class="brand-rule"></div>
  <h2 class="variety">Café<br>Tramo</h2>
  <div class="blend"><span class="blend-swatch"></span><p class="blend-ratio">60/40</p><p class="blend-detail">60%Arabica | 40%Robusta</p></div>
  <div class="beans-note"><svg viewBox="0 0 16 10"><circle cx="5" cy="5" r="4.5" fill="currentColor"/></svg>Ganze geröstete<br>Kaffeebohnen</div>
  <p class="address">Lindenkamp-Weg-Str. 7,<br>47618 Hollerbeck</p>
  <p class="web">www.tessuna.de</p>
  <p class="weight">℮1000 g<small>Kühl und trocken lagern</small></p>
</section>

<section class="label label--cafe" style="--swatch: var(--sorrel)">
  <div class="brand">TESSUNA</div>
  <div class="brand-rule"></div>
  <h2 class="variety">Café<br>Sorrel</h2>
  <div class="blend"><span class="blend-swatch"></span><p class="blend-ratio">70/30</p><p class="blend-detail">70%Arabica | 30%Robusta</p></div>
  <div class="beans-note"><svg viewBox="0 0 16 10"><circle cx="5" cy="5" r="4.5" fill="currentColor"/></svg>Ganze geröstete<br>Kaffeebohnen</div>
  <p class="address">Lindenkamp-Weg-Str. 7,<br>47618 Hollerbeck</p>
  <p class="web">www.tessuna.de</p>
  <p class="weight">℮1000 g<small>Kühl und trocken lagern</small></p>
</section>

<section class="label label--cafe" style="--swatch: var(--tiva)">
  <div class="brand">TESSUNA</div>
  <div class="brand-rule"></div>
  <h2 class="variety">Café<br>Tiva</h2>
  <div class="blend"><span class="blend-swatch"></span><p class="blend-ratio">80/20</p><p class="blend-detail">80%Arabica | 20%Robusta</p></div>
  <div class="beans-note"><svg viewBox="0 0 16 10"><circle cx="5" cy="5" r="4.5" fill="currentColor"/></svg>Ganze geröstete<br>Kaffeebohnen</div>
  <p class="address">Lindenkamp-Weg-Str. 7,<br>47618 Hollerbeck</p>
  <p class="web">www.tessuna.de</p>
  <p class="weight">℮1000 g<small>Kühl und trocken lagern</small></p>
</section>

<section class="label label--cafe" style="--swatch: var(--wisp)">
  <div class="brand">TESSUNA</div>
  <div class="brand-rule"></div>
  <h2 class="variety">Café<br>Wisp</h2>
  <div class="blend"><span class="blend-swatch"></span><p class="blend-ratio">100%</p><p class="blend-detail">100%Arabica</p></div>
  <div class="beans-note"><svg viewBox="0 0 16 10"><circle cx="5" cy="5" r="4.5" fill="currentColor"/></svg>Ganze geröstete<br>Kaffeebohnen</div>
  <p class="address">Lindenkamp-Weg-Str. 7,<br>47618 Hollerbeck</p>
  <p class="web">www.tessuna.de</p>
  <p class="weight">℮1000 g<small>Kühl und trocken lagern</small></p>
</section>

<section class="label label--espresso" style="--swatch: var(--vasto)">
  <div class="brand">TESSUNA</div>
  <div class="brand-rule"></div>
  <h2 class="variety">Espresso<br>Vasto</h2>
  <div class="blend"><span class="blend-swatch"></span><p class="blend-ratio">50/50</p><p class="blend-detail">50%Arabica | 50%Robusta</p></div>
  <div class="beans-note"><svg viewBox="0 0 16 10"><circle cx="5" cy="5" r="4.5" fill="currentColor"/></svg>Ganze geröstete<br>Kaffeebohnen</div>
  <p class="address">Lindenkamp-Weg-Str. 7,<br>47618 Hollerbeck</p>
  <p class="web">www.tessuna.de</p>
  <p class="weight">℮1000 g<small>Kühl und trocken lagern</small></p>
</section>

<section class="label label--espresso" style="--swatch: var(--calmora)">
  <div class="brand">TESSUNA</div>
  <div class="brand-rule"></div>
  <h2 class="variety">Espresso<br>Calmora</h2>
  <div class="blend"><span class="blend-swatch"></span><p class="blend-ratio">60/40</p><p class="blend-detail">60%Arabica | 40%Robusta</p></div>
  <div class="beans-note"><svg viewBox="0 0 16 10"><circle cx="5" cy="5" r="4.5" fill="currentColor"/></svg>Ganze geröstete<br>Kaffeebohnen</div>
  <p class="address">Lindenkamp-Weg-Str. 7,<br>47618 Hollerbeck</p>
  <p class="web">www.tessuna.de</p>
  <p class="weight">℮1000 g<small>Kühl und trocken lagern</small></p>
</section>

<section class="label label--espresso" style="--swatch: var(--nevio)">
  <div class="brand">TESSUNA</div>
  <div class="brand-rule"></div>
  <h2 class="variety">Espresso<br>Nevio</h2>
  <div class="blend"><span class="blend-swatch"></span><p class="blend-ratio">80/20</p><p class="blend-detail">80%Arabica | 20%Robusta</p></div>
  <div class="beans-note"><svg viewBox="0 0 16 10"><circle cx="5" cy="5" r="4.5" fill="currentColor"/></svg>Ganze geröstete<br>Kaffeebohnen</div>
  <p class="address">Lindenkamp-Weg-Str. 7,<br>47618 Hollerbeck</p>
  <p class="web">www.tessuna.de</p>
  <p class="weight">℮1000 g<small>Kühl und trocken lagern</small></p>
</section>

<section class="label label--espresso" style="--swatch: var(--brisa)">
  <div class="brand">TESSUNA</div>
  <div class="brand-rule"></div>
  <h2 class="variety">Brisa<br>Kalumetos</h2>
  <div class="blend"><span class="blend-swatch"></span><p class="blend-ratio blend-ratio--note">SPECIALLY ROASTED FOR</p><p class="blend-detail blend-detail--note">Freddo Espresso / Cappuccino</p></div>
  <div class="beans-note"><svg viewBox="0 0 16 10"><circle cx="5" cy="5" r="4.5" fill="currentColor"/></svg>Ganze geröstete<br>Kaffeebohnen</div>
  <p class="address">Lindenkamp-Weg-Str. 7,<br>47618 Hollerbeck</p>
  <p class="web">www.tessuna.de</p>
  <p class="weight">℮1000 g<small>Kühl und trocken lagern</small></p>
</section>

</body>
</html>
```